Need to create a website for a luxury custom home builder in Phoenix USA. Looking forward for some creative designs including a full page video intro on homepage and should show up pretty luxurious.

```html
<!DOCTYPE html>
<html lang="en">
<head>
<meta charset="UTF-8">
<title>Crestline Homes — Custom Luxury Homes</title>
<link rel="stylesheet" href="https://fonts.googleapis.com/css2?family=Krona+One&family=Montserrat:wght@400;500;600;700&display=swap">
<style>
:root{
  --teal:#2db597;
  --blue:#1ba6df;
  --sky:#2fc4ee;
  --ink:#1d1d1f;
  --grey:#5a5a5a;
  --pale:#e6f4fb;
  --line:#d9d9d9;
  --white:#ffffff;
}
*{margin:0;padding:0;box-sizing:border-box}
html,body{width:1200px;height:5186px;overflow:hidden;background:var(--white)}
body{position:relative;font-family:"Montserrat",sans-serif;color:var(--ink)}
.abs{position:absolute}
.display{font-family:"Krona One",sans-serif;letter-spacing:4px;text-transform:uppercase}
.eyebrow{font-size:11px;text-transform:uppercase;letter-spacing:.5px}
.copy{font-size:11.5px;line-height:18px}
.photo{position:absolute}

/* header */
.site-header{top:0;left:0;width:1200px;height:74px;background:var(--white)}
.brand{left:97px;top:18px;display:flex;align-items:center;gap:10px}
.brand-mark{width:30px;height:30px;border-radius:50%;background:var(--blue)}
.brand-name{font-weight:700;font-size:22px;color:var(--teal);letter-spacing:.5px;line-height:1}
.main-nav{left:350px;top:30px;display:flex;font-size:11px;font-weight:700;text-transform:uppercase}
.main-nav span{padding:0 22px;border-left:1px solid #bbb}
.main-nav span:first-child{border-left:none;padding-left:0}
.phone-bar{right:0;top:0;width:246px;height:74px;background:var(--teal);clip-path:polygon(28px 0,100% 0,100% 100%,0 100%);color:#fff;font-size:13px;font-weight:600;display:flex;align-items:center;padding-left:46px;gap:8px}

/* hero */
.hero-edge{top:74px;left:0;width:1200px;height:651px;background:var(--blue);clip-path:polygon(0 0,100% 0,100% 80%,50% 100%,0 82%)}
.hero-photo{top:74px;left:0;width:1200px;height:638px;background:linear-gradient(120deg,#3a3f45 0%,#5c5650 40%,#2c3138 75%,#1f2328 100%);clip-path:polygon(0 0,100% 0,100% 81%,50% 100%,0 82%)}
.hero-play{left:578px;top:244px}
.hero-title{left:0;top:328px;width:1200px;text-align:center;color:#fff;font-size:38px;line-height:42px;letter-spacing:6px}
.btn-solid{left:532px;top:452px;width:170px;height:44px;background:var(--blue);color:#fff;font-size:12px;font-weight:700;display:flex;align-items:center;justify-content:center;text-transform:uppercase;box-shadow:4px 4px 0 -1px #fff,4px 4px 0 0 var(--blue)}

/* custom homes */
.section-rule{left:0;top:808px;width:100px;height:2px;background:var(--blue)}
.section-title{left:120px;top:794px;font-size:24px}
.home-card{top:868px;height:340px}
.card-label{position:absolute;left:26px;bottom:30px;color:#fff;font-family:"Krona One",sans-serif;font-size:19px;letter-spacing:1px;text-transform:uppercase}
.card-label::after{content:"";display:block;width:36px;height:3px;background:#fff;margin-top:10px}
.card-active{background:var(--teal);color:#fff;padding:0 40px}
.card-active .arrow{position:absolute;left:132px;top:64px}
.card-active h3{position:absolute;left:40px;top:122px;font-family:"Krona One",sans-serif;font-weight:400;font-size:20px;letter-spacing:1px}
.card-active p{position:absolute;left:40px;top:170px;width:240px;font-size:12px;line-height:21px}
.btn-outline-w{position:absolute;left:42px;top:258px;width:150px;height:40px;border:2px solid #fff;color:#fff;font-size:12px;font-weight:700;display:flex;align-items:center;justify-content:center;text-transform:uppercase}
.dots{left:527px;top:1261px;display:flex;gap:4px}
.dots i{display:block;width:38px;height:3px;background:#cfd8dc}
.dots i:first-child{background:#3a4a55}

/* about */
.about-block{left:70px;top:1343px;width:296px;height:493px;background:var(--sky)}
.about-frame{left:107px;top:1379px;width:972px;height:429px;border:1px solid var(--blue);background:#fff}
.about-frame2{left:118px;top:1366px;width:978px;height:455px;border:1px solid var(--blue)}
.about-text{left:652px;top:1452px;width:370px}
.eyebrow.teal{color:var(--teal)}
.h2{font-family:"Krona One",sans-serif;font-size:24px;letter-spacing:3px;line-height:30px;text-transform:uppercase;margin:8px 0 20px}
.about-text .copy{color:var(--grey);margin-bottom:14px}
.btn-outline{display:inline-flex;width:150px;height:40px;border:2px solid var(--teal);color:var(--teal);font-size:12px;font-weight:700;align-items:center;justify-content:center;text-transform:uppercase;margin-top:10px}
.vrule{width:2px;background:var(--blue)}

/* build */
.build-panel{left:0;top:1947px;width:608px;height:499px;background:var(--teal);color:#fff}
.build-text{position:absolute;left:126px;top:104px;width:392px}
.build-text .copy{margin-bottom:14px}
.build-panel .btn-outline{border-color:#fff;color:#fff;margin-top:6px}

/* testimonials */
.center-title{left:0;width:1200px;text-align:center}
.testi-back{left:302px;top:2611px;width:656px;height:270px;border:1px solid var(--blue)}
.testi-box{left:290px;top:2599px;width:656px;height:270px;border:1px solid var(--blue);background:#fff;text-align:center;padding:30px 70px}
.testi-box p{font-size:13.5px;line-height:23px;color:#333;margin-top:20px}
.testi-box strong{display:block;margin-top:18px;font-size:14px}

/* gallery */
.gallery-band{left:0;top:2955px;width:1200px;height:465px;background:var(--pale)}
.ghost{font-family:"Krona One",sans-serif;font-size:60px;letter-spacing:8px;color:rgba(27,166,223,.14);text-transform:uppercase}
.nav-dot{width:40px;height:40px;border-radius:50%;background:var(--blue);display:flex;align-items:center;justify-content:center}

/* news */
.news-card{top:3825px;width:314px;height:372px;border:1px solid var(--line);background:#fff;text-align:center}
.news-card .thumb{position:absolute;left:8px;top:8px;width:296px;height:208px}
.date-tag{position:absolute;left:88px;top:202px;width:136px;height:26px;background:var(--teal);color:#fff;font-size:10px;font-weight:700;display:flex;align-items:center;justify-content:center}
.news-card h4{position:absolute;left:16px;top:240px;width:280px;font-size:11.5px;line-height:17px;font-weight:700;text-transform:uppercase}
.news-card p{position:absolute;left:30px;top:284px;width:252px;font-size:10.5px;line-height:16px;color:var(--grey)}
.news-card a{position:absolute;left:0;top:338px;width:100%;font-size:11px;font-weight:700;color:var(--blue);text-decoration:underline;letter-spacing:1px}

/* approach */
.approach-photo{left:0;top:4278px;width:700px;height:533px;background:linear-gradient(135deg,#d9d5cf 0%,#a9a39b 45%,#6d6862 80%,#4e4a46 100%)}
.approach-panel{left:503px;top:4278px;width:697px;height:533px;background:var(--blue);clip-path:polygon(0 0,100% 0,100% 100%,181px 100%)}
.approach-text{left:686px;top:4420px;width:380px;color:#fff}
.approach-text .btn-outline{border-color:#fff;color:#fff;width:172px;margin-top:22px;box-shadow:4px 4px 0 -1px var(--blue),4px 4px 0 0 #fff}

/* footer */
.footer-brand{left:155px;top:4908px;width:190px;text-align:center}
.footer-brand .brand-name{font-size:24px}
.social{display:flex;gap:8px;justify-content:center;margin-top:18px}
.social i{width:26px;height:26px;border:1.5px solid var(--teal);border-radius:50%;display:block}
.fcol{top:4811px;height:302px;border-left:1px solid var(--line);padding:86px 0 0 18px}
.fcol h5{font-size:12px;font-weight:700;text-transform:uppercase;position:relative}
.fcol h5::before{content:"";position:absolute;left:-18px;top:2px;width:3px;height:12px;background:var(--blue)}
.fcol ul{list-style:none;margin-top:18px;padding-left:8px}
.fcol li{font-size:11px;color:var(--grey);margin-bottom:10px}
.contact-row{display:flex;gap:10px;font-size:11px;line-height:16px;color:#333;margin-bottom:14px;align-items:flex-start}
.contact-row b{flex:none;width:22px;height:22px;border-radius:50%;background:var(--blue);display:flex;align-items:center;justify-content:center}
.footer-rule{left:0;top:5113px;width:1200px;height:1px;background:var(--line)}
.copyright{left:0;top:5140px;width:1200px;text-align:center;font-size:11px;color:var(--grey)}
</style>
</head>
<body>

<header class="abs site-header">
  <div class="abs brand"><span class="brand-mark"></span><span class="brand-name">CRESTLINE HOMES</span></div>
  <nav class="abs main-nav"><span>About Us</span><span>Services</span><span>Projects</span><span>Why Us</span><span>Blogs</span><span>Contact Us</span></nav>
  <div class="abs phone-bar">
    <svg width="16" height="16" viewBox="0 0 24 24" fill="none" stroke="#fff" stroke-width="2"><path d="M22 16.9v3a2 2 0 0 1-2.2 2 19.8 19.8 0 0 1-8.6-3.1 19.5 19.5 0 0 1-6-6A19.8 19.8 0 0 1 2.1 4.2 2 2 0 0 1 4.1 2h3a2 2 0 0 1 2 1.7c.1.9.4 1.8.7 2.7a2 2 0 0 1-.5 2.1L8 9.8a16 16 0 0 0 6 6l1.3-1.3a2 2 0 0 1 2.1-.4c.9.3 1.8.6 2.7.7a2 2 0 0 1 1.7 2z"/></svg>
    (480) 555 0192
  </div>
</header>

<section>
  <div class="abs hero-edge"></div>
  <div class="abs hero-photo" role="img" aria-label="Video still of a dark modern luxury living room with slatted wall panels and sofa"></div>
  <svg class="abs hero-play" width="64" height="64" viewBox="0 0 64 64"><circle cx="32" cy="32" r="29" fill="none" stroke="#fff" stroke-width="4"/><path d="M26 20 L44 32 L26 44Z" fill="#fff"/></svg>
  <h1 class="abs display hero-title">Building more than<br>dream luxury homes</h1>
  <div class="abs btn-solid">Contact Us</div>
</section>

<section>
  <div class="abs section-rule"></div>
  <h2 class="abs display section-title">Custom luxury homes</h2>
  <div class="abs home-card photo" style="left:111px;width:326px;background:linear-gradient(160deg,#4a3c2a,#7a6446 50%,#2b241b)" role="img" aria-label="Luxury living room with plants and warm lighting"><span class="card-label">Luxury Home</span></div>
  <div class="abs home-card card-active" style="left:443px;width:326px">
    <svg class="arrow" width="30" height="20" viewBox="0 0 30 20" fill="none" stroke="#fff" stroke-width="2"><path d="M2 10h24M18 3l8 7-8 7"/></svg>
    <h3>LUXURY HOME</h3>
    <p>Make vacation dreams come true with these spacious and exquisite Villas and Twinhomes</p>
    <div class="btn-outline-w">Learn More</div>
  </div>
  <div class="abs home-card photo" style="left:775px;width:324px;background:linear-gradient(170deg,#8fa2b8,#5a4a3e 55%,#2a2420)" role="img" aria-label="Modern luxury house exterior at dusk"><span class="card-label">Luxury Home</span></div>
  <div class="abs home-card photo" style="left:1109px;width:91px;background:linear-gradient(170deg,#d7c7a0,#a88a5e)" role="img" aria-label="Luxury house exterior"><span class="card-label">Luxur</span></div>
  <div class="abs dots"><i></i><i></i><i></i><i></i></div>
</section>

<section>
  <div class="abs about-frame2"></div>
  <div class="abs about-frame"></div>
  <div class="abs about-block"></div>
  <div class="abs photo" style="left:121px;top:1395px;width:459px;height:383px;background:linear-gradient(165deg,#b9c9dc 0%,#e8e8ea 45%,#c98a5a 70%,#5d6a6e 100%)" role="img" aria-label="White modern villa with warmly lit windows at twilight"></div>
  <div class="abs about-text">
    <div class="eyebrow teal">Who we are</div>
    <div class="h2">About Crestline<br>Homes</div>
    <p class="copy">Lorem ipsum dolor sit amet, consectetur adipiscing elit, sed do eiusmod tempor incididunt ut labore et dolore magna aliqua. Ut enim ad minim veniam, quis nostrud exercitation ullamco laboris nisi ut aliquip ex ea commodo consequat.</p>
    <p class="copy">Duis aute irure dolor in reprehenderit in voluptate velit esse cillum dolore eu fugiat nulla pariatur.</p>
    <span class="btn-outline">Learn More</span>
  </div>
  <div class="abs vrule" style="left:607px;top:1836px;height:66px"></div>
</section>

<section>
  <div class="abs build-panel">
    <div class="build-text">
      <div class="eyebrow">Who we are</div>
      <div class="h2">How we build<br>your home</div>
      <p class="copy">Lorem ipsum dolor sit amet, consectetur adipiscing elit, sed do eiusmod tempor incididunt ut labore et dolore magna aliqua. Ut enim ad minim veniam, quis nostrud exercitation ullamco laboris nisi ut aliquip ex ea commodo consequat.</p>
      <p class="copy">Duis aute irure dolor in reprehenderit in voluptate velit esse cillum dolore eu fugiat nulla pariatur.</p>
      <span class="btn-outline">Learn More</span>
    </div>
  </div>
  <div class="abs photo" style="left:608px;top:1947px;width:592px;height:499px;background:linear-gradient(120deg,#ffffff 0%,#eceeef 50%,#b9c4c8 80%,#8fa59a 100%)" role="img" aria-label="Architectural sketch blending into a finished modern house"></div>
  <div class="abs vrule" style="left:627px;top:2446px;height:44px"></div>
</section>

<section>
  <h2 class="abs display center-title" style="top:2532px;font-size:24px;color:var(--blue)">Testimonials</h2>
  <div class="abs testi-back"></div>
  <div class="abs testi-box">
    <svg width="44" height="32" viewBox="0 0 44 32"><path d="M2 2h16v14L10 30H4l6-12H2zM24 2h16v14l-8 14h-6l6-12h-8z" fill="var(--blue)"/></svg>
    <p>Lorem ipsum dolor sit amet, consectetur adipiscing elit, sed do eiusmod tempor incididunt ut labore et dolore magna aliqua. Ut enim ad minim veniam, quis nostrud exercitation ullamco laboris nisi ut aliquip ex ea commodo consequat. Duis aute irure dolor in reprehende</p>
    <strong>By Author Name</strong>
  </div>
  <svg class="abs" style="left:152px;top:2716px" width="42" height="28" viewBox="0 0 42 28" fill="none" stroke="#555" stroke-width="2.5"><path d="M40 14H4M16 2 4 14l12 12"/></svg>
  <svg class="abs" style="left:1042px;top:2716px" width="42" height="28" viewBox="0 0 42 28" fill="none" stroke="#555" stroke-width="2.5"><path d="M2 14h36M26 2l12 12-12 12"/></svg>
</section>

<section>
  <div class="abs gallery-band"></div>
  <div class="abs ghost center-title" style="top:3018px">Gallery</div>
  <h2 class="abs display center-title" style="top:3068px;font-size:24px">Latest projects</h2>
  <div class="abs photo" style="left:0;top:3144px;width:199px;height:242px;background:linear-gradient(180deg,#c9d6e0,#f0f0f0 45%,#2a8fa5)" role="img" aria-label="White villa with pool"></div>
  <div class="abs photo" style="left:217px;top:3247px;width:270px;height:272px;background:linear-gradient(150deg,#e9e3da,#b8ab98 60%,#7a6d5e)" role="img" aria-label="Living room with staircase"></div>
  <div class="abs photo" style="left:501px;top:3144px;width:270px;height:242px;background:linear-gradient(160deg,#d6d3cc,#8c7a62 55%,#4a4036)" role="img" aria-label="Double-height living room with chandelier"></div>
  <div class="abs photo" style="left:501px;top:3400px;width:270px;height:243px;background:linear-gradient(170deg,#c4d2dc,#c7653a 50%,#3a3e42)" role="img" aria-label="Modern house with orange accents and pool"></div>
  <div class="abs photo" style="left:801px;top:3247px;width:270px;height:272px;background:linear-gradient(170deg,#5a6e96,#6a5646 55%,#2a2420)" role="img" aria-label="Modern house at dusk"></div>
  <div class="abs photo" style="left:1097px;top:3160px;width:103px;height:242px;background:linear-gradient(170deg,#8fb0cf,#5f6e7c 60%,#3d4750)" role="img" aria-label="Modern house exterior"></div>
  <div class="abs nav-dot" style="left:50px;top:3245px"><svg width="20" height="14" viewBox="0 0 20 14" fill="none" stroke="#fff" stroke-width="2"><path d="M18 7H3M8 2 3 7l5 5"/></svg></div>
  <div class="abs nav-dot" style="left:1139px;top:3245px"><svg width="20" height="14" viewBox="0 0 20 14" fill="none" stroke="#fff" stroke-width="2"><path d="M2 7h15M12 2l5 5-5 5"/></svg></div>
</section>

<section>
  <div class="abs ghost center-title" style="top:3704px">News</div>
  <h2 class="abs display center-title" style="top:3752px;font-size:24px">Latest news</h2>
  <article class="abs news-card" style="left:125px">
    <div class="thumb" style="background:linear-gradient(160deg,#e6e1da,#b49a80 60%,#6c4a34)" role="img" aria-label="Bright living room interior"></div>
    <div class="date-tag">SEP 20, 2023</div>
    <h4>Sed ut perspiciatis unde omnis iste natus error sit</h4>
    <p>Lorem ipsum dolor sit amet, consectetur adipiscing elit, sed do eiusmod tempor incididunt ut labore et dolore magna</p>
    <a>LEARN MORE</a>
  </article>
  <article class="abs news-card" style="left:463px">
    <div class="thumb" style="background:linear-gradient(175deg,#cfdbe4,#eeeeee 45%,#2c95a8)" role="img" aria-label="Modern villa with pool"></div>
    <div class="date-tag">SEP 20, 2023</div>
    <h4>Sed ut perspiciatis unde omnis iste natus error sit</h4>
    <p>Lorem ipsum dolor sit amet, consectetur adipiscing elit, sed do eiusmod tempor incididunt ut labore et dolore magna</p>
    <a>LEARN MORE</a>
  </article>
  <article class="abs news-card" style="left:799px">
    <div class="thumb" style="background:linear-gradient(175deg,#6f86a8,#5c4b3d 55%,#2b2622)" role="img" aria-label="Modern house at twilight"></div>
    <div class="date-tag">SEP 20, 2023</div>
    <h4>Sed ut perspiciatis unde omnis iste natus error sit</h4>
    <p>Lorem ipsum dolor sit amet, consectetur adipiscing elit, sed do eiusmod tempor incididunt ut labore et dolore magna</p>
    <a>LEARN MORE</a>
  </article>
</section>

<section>
  <div class="abs photo approach-photo" role="img" aria-label="Elegant grey living room with coffered ceiling"></div>
  <div class="abs approach-panel"></div>
  <div class="abs approach-text">
    <div class="eyebrow">Our approach</div>
    <div class="h2">Uniquely designed<br>for what matters</div>
    <p class="copy">Lorem ipsum dolor sit amet, consectetur adipiscing elit, sed do eiusmod tempor incididunt ut labore et dolore magna aliqua. Ut enim ad minim veniam, quis nostrud exercitation ullamco laboris nisi ut aliquip ex ea commodo</p>
    <span class="btn-outline">Learn More</span>
  </div>
</section>

<footer>
  <div class="abs footer-brand">
    <span class="brand-name">CRESTLINE HOMES</span>
    <div class="social"><i></i><i></i><i></i></div>
  </div>
  <div class="abs fcol" style="left:423px;width:214px">
    <h5>Navigation</h5>
    <ul><li>About Us</li><li>Our Services</li><li>Projects</li><li>News</li><li>Contact Us</li></ul>
  </div>
  <div class="abs fcol" style="left:637px;width:232px">
    <h5>Resources</h5>
    <ul><li>Testimonials</li><li>Gallery</li><li>Terms of Use</li><li>Privacy Policy</li><li>Sitemap</li></ul>
  </div>
  <div class="abs fcol" style="left:869px;width:331px;padding-top:84px">
    <h5>Contact Us</h5>
    <div style="margin-top:16px">
      <div class="contact-row"><b><svg width="10" height="12" viewBox="0 0 10 12" fill="#fff"><path d="M5 0a4 4 0 0 0-4 4c0 3 4 8 4 8s4-5 4-8a4 4 0 0 0-4-4zm0 5.5A1.5 1.5 0 1 1 5 2.5a1.5 1.5 0 0 1 0 3z"/></svg></b><span>Suite 410, 2200 Camelback Rd,<br>Phoenix AZ 85016</span></div>
      <div class="contact-row"><b><svg width="11" height="11" viewBox="0 0 24 24" fill="#fff"><path d="M6.6 10.8a15 15 0 0 0 6.6 6.6l2.2-2.2a1 1 0 0 1 1-.2 11 11 0 0 0 3.6.6 1 1 0 0 1 1 1V20a1 1 0 0 1-1 1A17 17 0 0 1 3 4a1 1 0 0 1 1-1h3.5a1 1 0 0 1 1 1c0 1.2.2 2.4.6 3.6a1 1 0 0 1-.3 1z"/></svg></b><span style="padding-top:3px">(480) 555 0192</span></div>
      <div class="contact-row"><b><svg width="11" height="9" viewBox="0 0 22 16" fill="none" stroke="#fff" stroke-width="2"><rect x="1" y="1" width="20" height="14"/><path d="M1 1l10 8 10-8"/></svg></b><span style="padding-top:3px">hello@crestlinehomes.com</span></div>
    </div>
  </div>
  <div class="abs footer-rule"></div>
  <div class="abs copyright">Copyright © 2023 Crestline Homes. All rights reserved.</div>
</footer>

</body>
</html>
```